Medical Billing Business needs a web page designed

We need a web page for a new medical billing business for prospective clients to go to to get information about our company. It needs to show what our company stands for and our billing rates. Our colors are blue, gray and white. I have attached our logo, brochure and mission statement.

Need tabs at top for "about us", "contact us" "specials". On contact page, need a form to fill out that will be automatically emailed to us upon completion. Under specials...Sign a contract by the end of August 2014 and receive one month of billing FREE. ***Receive 25% off the first 4 months of the contract***

Medical

```html
<!DOCTYPE html>
<html lang="en">
<head>
<meta charset="utf-8">
<title>Prairie Ridge Billing</title>
<link href="https://fonts.googleapis.com/css2?family=Lato:wght@400;700&family=Oswald:wght@400;500&display=swap" rel="stylesheet">
<style>
:root{
  --teal:#1ab3c6;
  --teal-dark:#0f97a8;
  --teal-soft:#dff5f9;
  --gray:#6b6b6b;
  --gray-dark:#555;
  --gray-light:#f1f1f1;
  --text:#555;
  --white:#fff;
}
*{box-sizing:border-box;margin:0;padding:0}
html,body{width:968px;height:1200px;overflow:hidden;background:var(--white)}
body{font-family:"Lato",sans-serif;color:var(--text);position:relative}
.page{position:absolute;left:0;top:0;width:968px;height:1200px}
.abs{position:absolute}

/* header */
.brand{left:106px;top:30px;display:flex;align-items:center;gap:8px}
.brand-mark{width:22px;height:22px;background:var(--teal)}
.brand-name{font-size:19px;font-weight:700;color:var(--teal-dark);letter-spacing:.3px}
.social-top{right:106px;top:14px;display:flex;gap:8px}
.dot{width:25px;height:25px;border-radius:50%;background:var(--teal-dark)}
.contact-line{right:106px;font-size:14px;letter-spacing:1.6px;color:var(--gray-dark);font-weight:700;display:flex;align-items:center;gap:6px}

/* nav */
.nav{left:106px;top:104px;width:756px;height:30px;display:flex;background:var(--teal)}
.nav a{flex:1;text-decoration:none;color:#26444a;font-size:13.5px;display:flex;align-items:center;justify-content:center;border-left:1px solid #7fd7e2}
.nav a.active{flex:0 0 103px;background:var(--gray);color:var(--white);border:0;font-weight:700}

/* hero */
.hero{left:106px;top:134px;width:756px;height:272px;background:linear-gradient(90deg,#e9e1d9 0%,#d9c2ad 30%,#cfd4d8 60%,#e7ebee 100%)}
.arrow{top:105px;width:32px;height:38px;background:#9a9a9a;display:flex;align-items:center;justify-content:center}
.arrow.left{left:0;border-radius:0 19px 19px 0}
.arrow.right{right:0;border-radius:19px 0 0 19px}
.caption{left:82px;top:182px;width:605px;height:60px;background:rgba(26,179,198,.88);color:var(--white);font-family:"Oswald",sans-serif;font-size:26px;letter-spacing:1px;display:flex;align-items:center;justify-content:center}
.caption q{quotes:"\201C" "\201D"}
.hero-rule{left:106px;top:406px;width:756px;height:4px;background:var(--teal)}

/* features */
.features{left:106px;top:410px;width:756px;height:84px;background:linear-gradient(180deg,var(--teal-soft),var(--white))}
.feature{top:426px;width:189px;text-align:center}
.feature + .feature{border-left:1px dashed #bbb}
.feature svg{display:block;margin:0 auto}
.feature h3{margin-top:18px;font-size:14.5px;font-weight:400;color:var(--teal)}
.feature p{margin-top:14px;font-size:11px;line-height:16px;padding:0 6px}
.btn{display:inline-block;margin-top:20px;width:90px;height:25px;line-height:25px;background:var(--teal);color:#2c5a62;font-size:13.5px;border:1px solid #9adce5}

/* services */
.services{left:106px;top:680px;width:370px;height:315px;background:var(--gray-light)}
.services-head{height:40px;background:var(--teal);border-bottom:3px solid var(--teal-dark);display:flex;align-items:center;gap:8px;padding-left:10px;font-size:20px;color:#2c6f79}
.services ul{list-style:none;padding:8px 0 0 12px}
.services li{height:33.6px;display:flex;align-items:center;gap:10px;font-size:11px;color:#444}

/* specials */
.specials{left:491px;top:683px;width:365px;height:312px;background:var(--gray-light);overflow:hidden}
.specials svg{position:absolute;left:0;top:0}
.specials-lead{position:absolute;left:0;top:14px;width:365px;text-align:center;color:var(--white);font-size:21px;line-height:32px}
.specials-big{position:absolute;left:0;top:133px;width:365px;text-align:center;font-family:"Oswald",sans-serif;font-weight:500;font-size:46px;color:var(--teal-dark)}
.specials-note{position:absolute;left:0;top:206px;width:365px;text-align:center;color:var(--teal);font-size:27px;line-height:40px}

/* footer */
.footer{left:106px;top:1011px;width:756px;height:189px;background:linear-gradient(180deg,#7a7a7a,#5f5f5f);color:var(--white)}
.info{left:12px;display:flex;gap:10px;font-size:9.5px;line-height:13px}
.info b{display:block;color:var(--teal);font-weight:400;font-size:12.5px;line-height:15px}
.stay{left:252px;top:12px;font-size:14px}
.email-field{left:251px;top:36px;width:174px;height:23px;background:var(--white);border:1px solid #ccc;color:#777;font-size:11px;padding:4px 7px;letter-spacing:.5px}
.submit{left:251px;top:68px;width:68px;height:24px;background:var(--teal);color:var(--white);font-size:13px;font-weight:700;display:flex;align-items:center;justify-content:center;letter-spacing:.5px}
.footer-rule{left:252px;top:106px;width:213px;border-top:1px dashed #999}
.follow{left:252px;top:120px;display:flex;align-items:center;gap:8px;font-size:14px}
.follow .dot{width:25px;height:25px;background:#3f8fa8}
.map{left:488px;top:10px;width:253px;height:147px;background:linear-gradient(135deg,#eef0e6,#e2e6dc);border:2px solid #ddd}
.footer-links{left:0;top:159px;width:756px;height:30px;border-top:1px solid #777;display:flex;align-items:center;padding:0 10px;font-size:10px;gap:16px}
.footer-links .copy{margin-left:auto;letter-spacing:.3px}
</style>
</head>
<body>
<div class="page">

  <div class="abs brand"><span class="brand-mark"></span><span class="brand-name">Prairie Ridge Billing</span></div>

  <div class="abs social-top"><span class="dot"></span><span class="dot"></span><span class="dot"></span><span class="dot"></span></div>

  <div class="abs contact-line" style="top:51px">
    <svg width="14" height="16" viewBox="0 0 14 16"><path d="M3 1l3 3-2 2c1 2 3 4 5 5l2-2 3 3-2 3C6 15 0 8 1 3z" fill="#666"/></svg>
    (800)555-0142
  </div>
  <div class="abs contact-line" style="top:76px">
    <svg width="17" height="12" viewBox="0 0 17 12"><rect x="0.5" y="0.5" width="16" height="11" fill="#666"/><path d="M1 1l7.5 6L16 1" stroke="#fff" fill="none"/></svg>
    hello@prairieridgebill.com
  </div>

  <nav class="abs nav">
    <a class="active" href="#">HOME</a>
    <a href="#">Services</a>
    <a href="#">Solutions</a>
    <a href="#">Testimonials</a>
    <a href="#">Specials</a>
    <a href="#">About us</a>
    <a href="#">Contact us</a>
  </nav>

  <div class="abs hero" role="img" aria-label="Photo of a smiling team of doctors and nurses in white coats">
    <div class="abs arrow left"><svg width="8" height="10"><path d="M7 0v10L0 5z" fill="#fff"/></svg></div>
    <div class="abs arrow right"><svg width="8" height="10"><path d="M1 0v10l7-5z" fill="#fff"/></svg></div>
    <div class="abs caption"><q>&nbsp;A Uniquely Personal Approach to Health Care&nbsp;</q></div>
  </div>
  <div class="abs hero-rule"></div>

  <div class="abs features"></div>

  <div class="abs feature" style="left:106px">
    <svg width="62" height="74" viewBox="0 0 62 74"><path d="M2 4h58v34c0 18-14 28-29 34C16 66 2 56 2 38z" fill="var(--teal)" stroke="#0c8796" stroke-width="2"/><rect x="22" y="22" width="18" height="26" rx="2" fill="#2e6f78"/><rect x="25" y="25" width="12" height="5" fill="var(--teal)"/><g fill="var(--teal)"><rect x="25" y="33" width="3" height="3"/><rect x="30" y="33" width="3" height="3"/><rect x="35" y="33" width="2" height="3"/><rect x="25" y="39" width="3" height="3"/><rect x="30" y="39" width="3" height="3"/><rect x="35" y="39" width="2" height="3"/></g></svg>
    <h3>Medical Billing and Coding</h3>
    <p>Lorem ipsum dolor si consectetuer adipiscing elit, sed diam sgsv nonummy nibh euismod tinciduntzx dfxxfhc.</p>
    <span class="btn">Read More</span>
  </div>
  <div class="abs feature" style="left:295px">
    <svg width="62" height="74" viewBox="0 0 62 74"><path d="M2 4h58v34c0 18-14 28-29 34C16 66 2 56 2 38z" fill="var(--teal)" stroke="#0c8796" stroke-width="2"/><circle cx="31" cy="33" r="12" fill="none" stroke="#2e6f78" stroke-width="3"/><circle cx="31" cy="33" r="5" fill="#2e6f78"/><path d="M27 40h8l-4 9z" fill="#2e6f78"/></svg>
    <h3>Out of Network Billing</h3>
    <p>Lorem ipsum dolor si consectetuer adipiscing elit, sed diam sgsv nonummy nibh euasismod tinciduntzx dfxxfhdf as.</p>
    <span class="btn">Read More</span>
  </div>
  <div class="abs feature" style="left:484px">
    <svg width="62" height="74" viewBox="0 0 62 74"><path d="M2 4h58v34c0 18-14 28-29 34C16 66 2 56 2 38z" fill="var(--teal)" stroke="#0c8796" stroke-width="2"/><circle cx="31" cy="36" r="11" fill="none" stroke="#2e6f78" stroke-width="3"/><path d="M31 30v6l4 3" stroke="#2e6f78" stroke-width="2.5" fill="none"/><path d="M21 25l4-3M41 25l-4-3" stroke="#2e6f78" stroke-width="3"/></svg>
    <h3>Appointment Reminder</h3>
    <p>Lorem ipsum dolor si consectetuer adipiscing elit, seasd diam sgsv nonummy nibh asaseuismod tinciduntzx as dsfxxfhc.</p>
    <span class="btn">Read More</span>
  </div>
  <div class="abs feature" style="left:673px">
    <svg width="62" height="74" viewBox="0 0 62 74"><path d="M2 4h58v34c0 18-14 28-29 34C16 66 2 56 2 38z" fill="var(--teal)" stroke="#0c8796" stroke-width="2"/><rect x="19" y="26" width="24" height="20" fill="#2e6f78"/><path d="M19 26l4-5h16l4 5" fill="#2e6f78"/><path d="M28 30h6v5h3l-6 6-6-6h3z" fill="var(--teal)"/></svg>
    <h3>Free EMR Software</h3>
    <p>Lorem ipsum dolor si consectetuer adipiscing elit, sed diam sgsv nonummy nibh euasismod tincdutzx dfxxfhdf as.</p>
    <span class="btn">Read More</span>
  </div>

  <section class="abs services">
    <div class="services-head">
      <svg width="20" height="24" viewBox="0 0 20 24"><path d="M2 2h16v10c0 5-4 8-8 10C6 20 2 17 2 12z" fill="none" stroke="#2c6f79" stroke-width="2"/></svg>
      Our Services
    </div>
    <ul>
      <li><svg width="16" height="16" viewBox="0 0 16 16"><circle cx="8" cy="8" r="6.5" fill="none" stroke="#555" stroke-width="1.5"/><path d="M4.5 8l2.5 2.5L15 2" stroke="#555" stroke-width="2" fill="none"/></svg>Lorem ipsum dolor si consectetuer adipiscing elit, sed diam sgsv.</li>
      <li><svg width="16" height="16" viewBox="0 0 16 16"><circle cx="8" cy="8" r="6.5" fill="none" stroke="#555" stroke-width="1.5"/><path d="M4.5 8l2.5 2.5L15 2" stroke="#555" stroke-width="2" fill="none"/></svg>Ssda Lorem ipsum dolasdor si consectetuer strfd adipiscing.</li>
      <li><svg width="16" height="16" viewBox="0 0 16 16"><circle cx="8" cy="8" r="6.5" fill="none" stroke="#555" stroke-width="1.5"/><path d="M4.5 8l2.5 2.5L15 2" stroke="#555" stroke-width="2" fill="none"/></svg>Lms ipsum dolor si consectetuer adipiscing elit, sed diam end.</li>
      <li><svg width="16" height="16" viewBox="0 0 16 16"><circle cx="8" cy="8" r="6.5" fill="none" stroke="#555" stroke-width="1.5"/><path d="M4.5 8l2.5 2.5L15 2" stroke="#555" stroke-width="2" fill="none"/></svg>Ipsum dolor si consectetuer Lorem adipiscing elit, sed diam sg.</li>
      <li><svg width="16" height="16" viewBox="0 0 16 16"><circle cx="8" cy="8" r="6.5" fill="none" stroke="#555" stroke-width="1.5"/><path d="M4.5 8l2.5 2.5L15 2" stroke="#555" stroke-width="2" fill="none"/></svg>Dolor si consectetuer Lorem ipsum adipiscing elit, sed diam sgsv.</li>
      <li><svg width="16" height="16" viewBox="0 0 16 16"><circle cx="8" cy="8" r="6.5" fill="none" stroke="#555" stroke-width="1.5"/><path d="M4.5 8l2.5 2.5L15 2" stroke="#555" stroke-width="2" fill="none"/></svg>Consectetuer adipiscing elit, sed Lorem ipsum &nbsp;a dolor si diam.</li>
      <li><svg width="16" height="16" viewBox="0 0 16 16"><circle cx="8" cy="8" r="6.5" fill="none" stroke="#555" stroke-width="1.5"/><path d="M4.5 8l2.5 2.5L15 2" stroke="#555" stroke-width="2" fill="none"/></svg>Ctetuer lorem ipsum dolor si conseadipiscing elit, sed diam sg.</li>
      <li><svg width="16" height="16" viewBox="0 0 16 16"><circle cx="8" cy="8" r="6.5" fill="none" stroke="#555" stroke-width="1.5"/><path d="M4.5 8l2.5 2.5L15 2" stroke="#555" stroke-width="2" fill="none"/></svg>Tetuer adipiscing elit, sed lorem ipsum dolor si consec diam.</li>
    </ul>
  </section>

  <section class="abs specials">
    <svg width="365" height="312" viewBox="0 0 365 312"><path d="M0 0h365v100C300 150 190 175 60 178 30 178 12 175 0 170z" fill="var(--teal)"/></svg>
    <div class="specials-lead">Sign a contract by the end of<br>August 2014 and receive one<br>month of billing FREE</div>
    <div class="specials-big">25% OFF</div>
    <div class="specials-note">Receive 25% off the first 4<br>months of the contract</div>
  </section>

  <footer class="abs footer">
    <div class="abs info" style="top:14px">
      <svg width="32" height="32" viewBox="0 0 32 32"><circle cx="16" cy="16" r="13" fill="none" stroke="var(--teal)" stroke-width="1.5"/><path d="M16 8v8h6" stroke="var(--teal)" stroke-width="1.5" fill="none"/></svg>
      <div><b>Open everyday</b>from 12a.m. to 2:15p.m.<br>and 6p.m. to midnight</div>
    </div>
    <div class="abs info" style="top:68px">
      <svg width="32" height="22" viewBox="0 0 32 22"><path d="M2 2h16v10H8l-4 4v-4H2z" fill="var(--teal)"/><path d="M12 8h16v10h-2v4l-4-4H12z" fill="var(--teal)"/></svg>
      <div style="padding-top:2px"><b style="display:inline">Appointment</b> at (800)555-0142</div>
    </div>
    <div class="abs info" style="top:105px">
      <svg width="32" height="22" viewBox="0 0 32 22"><path d="M16 0a7 7 0 017 7c0 5-7 13-7 13S9 12 9 7a7 7 0 017-7z" fill="var(--teal)"/><circle cx="16" cy="7" r="2.5" fill="#666"/></svg>
      <div><b>Prairie Ridge Billing</b>480 W Elm Street<br>Cedarton KS 66000</div>
    </div>

    <div class="abs stay">Stay in Touch</div>
    <div class="abs email-field">Enter your email here</div>
    <div class="abs submit">SUBMIT</div>
    <div class="abs footer-rule"></div>
    <div class="abs follow">Follow us <span class="dot"></span><span class="dot"></span><span class="dot"></span><span class="dot"></span></div>

    <div class="abs map" role="img" aria-label="Road map showing the office location with a red pin"></div>

    <div class="abs footer-links">
      <span>Home</span><span>Services</span><span>Solution</span><span>Testimonial</span><span>Specials</span><span>Contact us</span><span>About us</span>
      <span class="copy">© 2014 PrairieRidgeBill. All Rights Reserved</span>
    </div>
  </footer>

</div>
</body>
</html>
```